Business cards

We need a logo design for 2 new business card. One design for two brands "De Kolk" and Brivo Helpdesk. We are looking for a creative and fun way to show our clients that we are one company. De color Red is te color of "De Kolk" The color orange (FF6600) is the color for Brivo Helpdesk. in combination with the color white. Font is Sikina (google).
Both brands are working for entrepreneurs en small business owners in the Netherlands. De Kolk is a magazine and Brivo Helpdesk is a online platform where business owners can download white papers, books, do scans and can read artikels about entrepreneurship.
our pay of is : Antwoord op ondernemers vragen

```html
<!DOCTYPE html>
<html lang="en">
<head>
<meta charset="utf-8">
<title>Brivo Helpdesk business cards</title>
<link rel="stylesheet" href="https://fonts.googleapis.com/css2?family=Ubuntu:wght@400;500;700&display=swap">
<style>
  :root {
    --backdrop: #1f1f1f;
    --card-white: #f4f4f4;
    --band-dark: #232223;
    --brand-orange: #ff6600;
    --orange-deep: #e9711c;
    --text-dark: #3a3a3a;
    --text-light: #f1f1f1;
    --map-grey: #d6d6d6;
  }
  * { box-sizing: border-box; margin: 0; padding: 0; }
  html, body { width: 1200px; height: 1000px; overflow: hidden; }
  body {
    background: var(--backdrop);
    font-family: "Ubuntu", sans-serif;
    position: relative;
  }
  .card {
    position: absolute;
    top: 355px;
    width: 500px;
    height: 290px;
    border-radius: 18px;
    overflow: hidden;
    background: var(--card-white);
  }
  .card--front { left: 70px; }
  .card--back { left: 630px; }

  .world-map {
    position: absolute;
    background: var(--map-grey);
    opacity: .5;
    border-radius: 30px 50px 24px 60px;
    z-index: 0;
  }

  /* front */
  .front-band {
    position: absolute;
    left: 0; right: 0;
    top: 70px; height: 112px;
    background: var(--band-dark);
  }
  .card--front .world-map { left: 360px; top: 192px; width: 115px; height: 80px; }
  .name-tag {
    position: absolute;
    left: 45px; top: 52px;
    width: 265px; height: 58px;
    background: var(--orange-deep);
    border-radius: 10px;
    padding: 9px 0 0 40px;
    color: #fff;
    z-index: 1;
  }
  .name-tag__name { font-weight: 700; font-size: 18px; line-height: 1.1; }
  .name-tag__role { font-size: 14px; color: #2a1a0c; }
  .direct-contact {
    position: absolute;
    left: 85px; top: 122px;
    color: var(--text-light);
    font-size: 16px;
    line-height: 1.3;
    z-index: 1;
  }
  .office {
    position: absolute;
    left: 85px; top: 200px;
    color: var(--text-dark);
    font-size: 13.5px;
    line-height: 1.35;
    z-index: 1;
  }
  .office__line { display: flex; align-items: center; gap: 8px; }
  .office__address { margin-bottom: 4px; }
  .icon-box {
    width: 15px; height: 13px;
    background: #4a4a4a;
    border-radius: 2px;
    display: inline-flex; align-items: center; justify-content: center;
  }

  /* back */
  .back-band {
    position: absolute;
    left: 0; right: 0;
    top: 150px; bottom: 0;
    background: var(--band-dark);
  }
  .card--back .world-map { left: 170px; top: 18px; width: 300px; height: 92px; }
  .brand-name {
    position: absolute;
    left: 70px; top: 122px;
    display: flex; align-items: center; gap: 14px;
    z-index: 1;
  }
  .brand-name__square {
    width: 40px; height: 40px;
    background: var(--brand-orange);
    border-radius: 4px;
  }
  .brand-name__text {
    font-weight: 700;
    font-size: 40px;
    color: var(--brand-orange);
    letter-spacing: -0.5px;
  }
  .web-address {
    position: absolute;
    left: 124px; top: 190px;
    color: #bdbdbd;
    font-size: 15px;
    z-index: 1;
  }
</style>
</head>
<body>
  <section class="card card--front">
    <div class="front-band"></div>
    <div class="world-map" role="img" aria-label="Dotted world map in light grey"></div>
    <div class="name-tag">
      <p class="name-tag__name">Ruben Vermeer</p>
      <p class="name-tag__role">accountant</p>
    </div>
    <div class="direct-contact">
      <p>+31 30 555 0142</p>
      <p>ruben@brivohelpdesk.com</p>
    </div>
    <div class="office">
      <p class="office__address">12 Kanaalweg, 3526 Utrecht, Nederland.</p>
      <p class="office__line">
        <span class="icon-box">
          <svg width="11" height="10" viewBox="0 0 11 10"><path d="M2 1 L4 1 L4.6 3 L3.4 3.8 Q4.5 6 6.8 6.8 L7.6 5.6 L9.6 6.2 L9.6 8.4 Q4 9 1.6 2.6 Z" fill="#fff"/></svg>
        </span>
        +31 (0) 20 555 0199
      </p>
      <p class="office__line">
        <span class="icon-box">
          <svg width="11" height="9" viewBox="0 0 11 9"><rect x="0.8" y="0.8" width="9.4" height="7.4" fill="none" stroke="#fff" stroke-width="1"/><path d="M0.8 0.8 L5.5 5 L10.2 0.8" fill="none" stroke="#fff" stroke-width="1"/></svg>
        </span>
        info@brivohelpdesk.com
      </p>
    </div>
  </section>

  <section class="card card--back">
    <div class="back-band"></div>
    <div class="world-map" role="img" aria-label="Dotted world map in light grey"></div>
    <div class="brand-name">
      <span class="brand-name__square"></span>
      <span class="brand-name__text">brivohelpdesk</span>
    </div>
    <p class="web-address">www.brivohelpdesk.com</p>
  </section>
</body>
</html>
```